Corvel Ashdane Website

Updated website for Corvel Ashdane Dry Cleaners & Garment Care.

Please look at www.tindalecleaners.com we really like this site!!!

We are not set on colors or fonts. Looking for an professional easy to use site that looks and works even better on a mobile device. 90% of our customers visit us on cell phones.

Target Market(s)

We are located in an up scale area with young trendy individuals but, also very successful mature customers as well. Probably geared more to tech savvy younger crowd.

Industry/Entity Type

Dry Cleaning

Coding

Coded - Design and coding required

Font styles to use
Serif
Script

Colors
85abd2
85cae6
cee9f5
cfdeed
757575

Requirements
Must have
• Must look good on a mobile device and have sign up for our pick up and delivery. Geographical pick up and delivery perimeters would be great as well. Capturing emails and other user data for future marketing. We do a lot of advertising.
• Please look at www.tindalecleaners.com we really like this site!!!
• Search engine optimized.
• Also we are adding a new POS system that will have a login for customers and possibly an app.
Nice to have
• 100% satisfaction guaranteed and scrolling reviews somewhere on the page.

```html
<!DOCTYPE html>
<html lang="en">
<head>
<meta charset="utf-8">
<title>Corvel Ashdane Dry Cleaners &amp; Garment Care</title>
<link href="https://fonts.googleapis.com/css2?family=Lobster+Two:ital,wght@1,700&family=Open+Sans:wght@400;600;700&display=swap" rel="stylesheet">
<style>
:root{
  --sky:#85cae6;
  --sky-deep:#6fbde0;
  --steel:#85abd2;
  --mist:#cee9f5;
  --haze:#cfdeed;
  --ink:#2b3240;
  --text:#757575;
  --footer:#3c424e;
  --footer-text:#c9ced6;
  --white:#ffffff;
}
*{margin:0;padding:0;box-sizing:border-box}
html,body{width:1200px;height:3273px;overflow:hidden}
body{position:relative;font-family:"Open Sans",Arial,sans-serif;color:var(--text);background:var(--white)}
.abs{position:absolute}
.script{font-family:"Lobster Two",Georgia,serif;font-style:italic;font-weight:700}
.btn{position:absolute;display:flex;align-items:center;justify-content:center;font-size:12px;color:var(--white);background:var(--steel);border-radius:2px}
.btn-ghost{background:transparent;border:1.5px solid var(--sky);color:var(--sky-deep)}

/* hero */
.hero{position:absolute;left:0;top:0;width:1200px;height:640px;background:linear-gradient(100deg,#6b5a52 0%,#8d7466 25%,#a18a7d 50%,#8e8079 72%,#6d6662 100%)}
.hero-shade{position:absolute;inset:0;background:rgba(40,30,28,.35)}
.brand{position:absolute;left:78px;top:26px;display:flex;align-items:center;gap:12px}
.brand-dot{width:50px;height:50px;border-radius:50%;background:var(--mist)}
.brand-name{font-size:17px;font-weight:700;color:var(--white)}
.nav{position:absolute;top:42px;left:420px;display:flex;gap:26px;font-size:13px;color:var(--white)}
.nav .active{color:var(--sky)}
.login{position:absolute;left:916px;top:42px;font-size:13px;color:var(--white);display:flex;gap:6px;align-items:center}
.hero-title{position:absolute;top:200px;width:100%;text-align:center;font-size:40px;color:var(--white)}
.zip{position:absolute;left:385px;top:280px;width:430px;height:40px;background:var(--white);border-radius:2px;display:flex;align-items:center}
.zip span{padding-left:14px;font-size:12px;color:#999;flex:1}
.zip b{width:114px;height:34px;margin-right:3px;background:var(--sky-deep);color:var(--white);font-size:12px;font-weight:600;display:flex;align-items:center;justify-content:center;border-radius:2px}
.serving{position:absolute;top:346px;width:100%;text-align:center;font-size:15px;font-weight:600;color:var(--white)}
.store{position:absolute;top:410px;width:184px;height:54px;background:#111;border:1.5px solid #ddd;border-radius:6px;color:var(--white);display:flex;flex-direction:column;justify-content:center;padding-left:56px}
.store small{font-size:10px}
.store strong{font-size:17px;font-weight:600}
.store i{position:absolute;left:14px;top:13px;width:28px;height:28px;border-radius:4px;background:#444}

/* why */
.why{position:absolute;top:640px;left:0;width:1200px;height:399px;background:#f3f4f7}
.section-title{position:absolute;width:100%;text-align:center;font-size:38px;color:var(--ink)}
.feature{position:absolute;top:130px;width:240px;text-align:center}
.feature .ring{width:96px;height:96px;margin:0 auto;border-radius:50%;border:2px solid var(--mist);background:var(--white);display:flex;align-items:center;justify-content:center}
.feature .ring.on{background:var(--sky);border-color:var(--sky)}
.feature p{margin-top:20px;font-size:15px;color:#444}

/* about */
.about{position:absolute;top:1039px;left:0;width:1200px;height:401px;background:var(--white)}
.about h2{position:absolute;left:155px;top:76px;font-size:36px;color:var(--ink)}
.about p{position:absolute;left:155px;top:142px;width:400px;font-size:12.5px;line-height:1.6}
.about-photo{position:absolute;left:612px;top:0;width:433px;height:401px;background:linear-gradient(180deg,#5fa3e4 0%,#8dbfe9 45%,#7a6a5c 62%,#4f8a3e 80%,#6f7275 100%)}

/* services */
.services{position:absolute;top:1440px;left:0;width:1200px;height:574px;background:linear-gradient(120deg,#1f1e1f 0%,#3a3b40 40%,#2b2c30 70%,#1b1b1c 100%)}
.services .section-title{color:var(--white);top:52px}
.card{position:absolute;top:135px;width:222px;height:300px;border-left:1px solid rgba(255,255,255,.35);padding:0 22px}
.card.last{border-right:1px solid rgba(255,255,255,.35);width:1px;padding:0}
.card h3{margin-top:80px;font-size:22px;font-weight:600;line-height:1.2;color:var(--white)}
.card p{margin-top:18px;font-size:12px;line-height:1.55;color:#e4e4e4}
.card .go{position:absolute;left:22px;top:258px;width:26px;height:26px;border-radius:50%;border:1.5px solid #ddd;display:flex;align-items:center;justify-content:center}
.card .go.on{background:var(--sky);border-color:var(--sky)}
.card svg.icon{position:absolute;left:22px;top:22px}
.arrow{position:absolute;font-size:26px;color:var(--white)}

/* guarantee */
.guarantee{position:absolute;top:2014px;left:0;width:1200px;height:360px;background:linear-gradient(90deg,#f1efed 0%,#eceae7 38%,#d9c9b2 55%,#b7c6d4 75%,#9fb9d2 100%)}
.guarantee h2{position:absolute;left:155px;top:120px;font-size:35px;color:var(--ink)}
.guarantee h2 span{color:var(--sky-deep)}
.guarantee p{position:absolute;left:155px;top:184px;width:540px;font-size:15px;line-height:1.5;color:#333}

/* testimonials */
.testimonials{position:absolute;top:2374px;left:0;width:1200px;height:445px;background:var(--white)}
.review{position:absolute;top:130px;width:255px}
.review .face{width:98px;height:98px;border-radius:50%;border:3px solid var(--mist);background:linear-gradient(160deg,#d9c6b6,#9e8c80)}
.review p{margin-top:22px;font-size:12px;line-height:1.55;color:#555}
.review .name{margin-top:14px;font-size:13px;color:var(--steel)}
.review .role{font-size:10px;color:#888}

/* footer */
.footer{position:absolute;top:2819px;left:0;width:1200px;height:454px;background:var(--footer);color:var(--footer-text);font-size:12px}
.footer .brand{left:155px;top:74px}
.footer h4{position:absolute;top:92px;font-size:16px;font-weight:400;color:var(--white)}
.footer ul{position:absolute;top:146px;list-style:none;line-height:22.5px}
.call{position:absolute;left:155px;top:150px;font-size:17px;color:var(--sky)}
.call b{color:var(--white);font-weight:400}
.social{position:absolute;left:1000px;width:40px;height:40px;border-radius:50%;border:1.5px solid #9aa0aa}
.social.on{background:var(--sky);border-color:var(--sky)}
.rule{position:absolute;left:155px;top:366px;width:890px;height:1px;background:rgba(255,255,255,.08)}
.badge{position:absolute;left:762px;top:382px;width:130px;height:46px;background:#1f5c8c;border-radius:2px}
.up{position:absolute;left:998px;top:386px;width:44px;height:44px;border-radius:50%;background:var(--steel);display:flex;align-items:center;justify-content:center}
</style>
</head>
<body>

<header class="hero">
  <div class="hero-shade" role="img" aria-label="Photo of garments hanging on a rail in a clothing shop"></div>
  <div class="brand"><span class="brand-dot"></span><span class="brand-name">Corvel Ashdane</span></div>
  <nav class="nav"><span class="active">Home</span><span>About Us</span><span>Pick Up &amp; Delivery</span><span>Services</span><span>Contact Us</span></nav>
  <div class="login"><svg width="11" height="12" viewBox="0 0 11 12"><circle cx="5.5" cy="3.5" r="3" fill="#fff"/><path d="M0 12a5.5 5 0 0 1 11 0z" fill="#fff"/></svg>Login</div>
  <div class="btn" style="left:992px;top:34px;width:126px;height:34px;background:var(--sky-deep)">Schedule Pick-Up</div>
  <h1 class="hero-title script">Dry Cleaning &amp; Garment Experts</h1>
  <div class="zip"><span>Enter Your Zip Code ...</span><b>Get Started</b></div>
  <p class="serving">We serving by Lakemont</p>
  <div class="store" style="left:410px"><i></i><small>Get the app on</small><strong>Pocket Market</strong></div>
  <div class="store" style="left:607px"><i></i><small>Available on the</small><strong>App Shelf</strong></div>
  <svg class="abs" style="left:594px;top:588px" width="12" height="8" viewBox="0 0 12 8"><path d="M1 1l5 5 5-5" stroke="#fff" stroke-width="2" fill="none"/></svg>
</header>

<section class="why">
  <h2 class="section-title script" style="top:50px">Why Choose Us</h2>
  <div class="feature" style="left:175px">
    <div class="ring"><svg width="42" height="30" viewBox="0 0 42 30"><path d="M2 4h24v18H2zM26 10h8l6 7v5H26z" fill="none" stroke="var(--sky-deep)" stroke-width="2"/><circle cx="10" cy="24" r="4" fill="#fff" stroke="var(--sky-deep)" stroke-width="2"/><circle cx="32" cy="24" r="4" fill="#fff" stroke="var(--sky-deep)" stroke-width="2"/></svg></div>
    <p>Free Pick Up &amp; Delivery</p>
  </div>
  <div class="feature" style="left:480px">
    <div class="ring on"><svg width="36" height="36" viewBox="0 0 36 36"><path d="M4 16h7v17H4zM13 17l7-13c3 0 4 2 3 6l-1 4h9c2 0 3 2 3 4l-3 12c-1 2-2 3-4 3H13z" fill="#fff"/></svg></div>
    <p>Unmatched Quality</p>
  </div>
  <div class="feature" style="left:785px">
    <div class="ring"><svg width="34" height="36" viewBox="0 0 34 36"><path d="M10 3l7 5 7-5 8 6-4 6v18H6V15L2 9z" fill="none" stroke="var(--sky-deep)" stroke-width="2"/><path d="M17 8v25" stroke="var(--sky-deep)" stroke-width="2"/></svg></div>
    <p>Toxin-Free Dry Cleaning</p>
  </div>
  <div class="btn btn-ghost" style="left:535px;top:300px;width:130px;height:32px">Sign up Here!</div>
</section>

<section class="about">
  <h2 class="script">About Us</h2>
  <p>Our passion started well over 50 years ago with our original store 'Fennick' which was located in the heart of Downtown Lakemont, where Pier Row stands today. We have now been in Lakemont for over 36 years! We are a family owned and operated business that provides quality and exceptional service.&nbsp; We take pride in our work and it shows!</p>
  <div class="btn" style="left:155px;top:281px;width:128px;height:33px">Discover More</div>
  <div class="about-photo" role="img" aria-label="Photo of the dry cleaning storefront with a garden and lawn in front"></div>
</section>

<section class="services" role="region" aria-label="Our Services">
  <div class="abs" style="inset:0" role="img" aria-label="Dark background photo of a folded dress shirt"></div>
  <h2 class="section-title script">Our Services</h2>
  <span class="arrow" style="left:110px;top:272px">&#8249;</span>
  <span class="arrow" style="left:1068px;top:272px">&#8250;</span>

  <div class="card" style="left:155px">
    <svg class="icon" width="40" height="40" viewBox="0 0 40 40"><path d="M20 6a3 3 0 1 1 3 3c-2 0-3 1-3 3v2L4 26h32L20 14" fill="none" stroke="var(--sky)" stroke-width="2.2"/><path d="M8 28h24v8H8z" fill="var(--sky)"/></svg>
    <h3>Dry<br>Cleaning</h3>
    <p>At Corvel Ashdane we specialize in dry cleaning of high-end clothing and fine linens. Our plant is ...</p>
    <span class="go"><svg width="10" height="10" viewBox="0 0 10 10"><path d="M1 5h8M6 2l3 3-3 3" stroke="#fff" stroke-width="1.4" fill="none"/></svg></span>
  </div>
  <div class="card" style="left:378px">
    <svg class="icon" width="40" height="40" viewBox="0 0 40 40"><path d="M13 4l7 5 7-5 10 7-5 7-3-2v20H11V16l-3 2-5-7z" fill="var(--sky)"/><path d="M20 9v25" stroke="#2d2e32" stroke-width="1.5"/></svg>
    <h3>Shirt<br>Laundering</h3>
    <p>Bringing your shirts to Corvel Ashdane Drycleaners will help you look your professional best ...</p>
    <span class="go on"><svg width="10" height="10" viewBox="0 0 10 10"><path d="M1 5h8M6 2l3 3-3 3" stroke="#fff" stroke-width="1.4" fill="none"/></svg></span>
  </div>
  <div class="card" style="left:600px">
    <svg class="icon" width="40" height="40" viewBox="0 0 40 40"><path d="M14 14a6 6 0 0 1 12 0" fill="none" stroke="var(--sky)" stroke-width="2.2"/><path d="M7 14h26l3 22H4z" fill="var(--sky)"/></svg>
    <h3>Suede<br>&amp; Leather</h3>
    <p>Suede and Leather need a special kind of cleaning.&nbsp; Cleaning these precious items is a delicate ...</p>
    <span class="go"><svg width="10" height="10" viewBox="0 0 10 10"><path d="M1 5h8M6 2l3 3-3 3" stroke="#fff" stroke-width="1.4" fill="none"/></svg></span>
  </div>
  <div class="card" style="left:820px">
    <svg class="icon" width="40" height="40" viewBox="0 0 40 40"><rect x="6" y="4" width="28" height="9" rx="2" fill="var(--sky)"/><rect x="6" y="15" width="28" height="9" rx="2" fill="var(--sky)"/><rect x="6" y="26" width="28" height="9" rx="2" fill="var(--sky)"/></svg>
    <h3>Wash<br>&amp; Fold</h3>
    <p>Life can be hectic.&nbsp; Let us help you with your laundry! Give us your dirty laundry and we will wash it ...</p>
    <span class="go"><svg width="10" height="10" viewBox="0 0 10 10"><path d="M1 5h8M6 2l3 3-3 3" stroke="#fff" stroke-width="1.4" fill="none"/></svg></span>
  </div>
  <div class="card last" style="left:1045px"></div>
  <div class="btn btn-ghost" style="left:527px;top:478px;width:146px;height:34px;color:#fff">View All Services</div>
</section>

<section class="guarantee">
  <div class="abs" style="left:560px;top:0;width:640px;height:360px" role="img" aria-label="Photo of two women laughing on a bicycle by the seaside"></div>
  <svg class="abs" style="left:155px;top:60px" width="46" height="46" viewBox="0 0 46 46"><circle cx="23" cy="23" r="21" fill="var(--sky)"/><circle cx="23" cy="23" r="13" fill="none" stroke="#fff" stroke-width="2"/><path d="M17 23l4 4 8-8" stroke="#fff" stroke-width="2.5" fill="none"/></svg>
  <h2 class="script"><span>100%</span> Satisfaction Guarantee</h2>
  <p>If you're ever unhappy with the quality of our dry cleaning or pressing, we'll redo the item for free!</p>
  <div class="btn" style="left:155px;top:261px;width:128px;height:35px">Contact Us</div>
</section>

<section class="testimonials">
  <h2 class="section-title script" style="top:52px">Testimonials</h2>
  <span class="arrow" style="left:100px;top:262px;color:#444">&#8249;</span>
  <span class="arrow" style="left:1088px;top:262px;color:#444">&#8250;</span>
  <div class="review" style="left:155px">
    <div class="face" role="img" aria-label="Customer portrait"></div>
    <p>"There are many variations of passages of Lorem Ipsum available, but the majority have suffered alteration in some form, by injected humour.</p>
    <div class="name">Standard Chunk</div><div class="role">Accompanied</div>
  </div>
  <div class="review" style="left:460px">
    <div class="face" role="img" aria-label="Customer portrait"></div>
    <p>"There are many variations of passages of Lorem Ipsum available, but the majority have suffered alteration in some form, by injected humour.</p>
    <div class="name">Standard Chunk</div><div class="role">Accompanied</div>
  </div>
  <div class="review" style="left:765px">
    <div class="face" role="img" aria-label="Customer portrait"></div>
    <p>"There are many variations of passages of Lorem Ipsum available, but the majority have suffered alteration in some form, by injected humour.</p>
    <div class="name">Standard Chunk</div><div class="role">Accompanied</div>
  </div>
</section>

<footer class="footer">
  <div class="brand"><span class="brand-dot"></span><span class="brand-name">Corvel Ashdane</span></div>
  <div class="call">Call Us: <b>(612) 555-0148</b></div>
  <div class="abs" style="left:155px;top:180px;color:var(--sky);text-decoration:underline">info@corvelashdanecleaners.com</div>
  <div class="abs" style="left:155px;top:212px;line-height:1.6">218 Harbor Lane, Lakemont,<br>ST 00412</div>
  <div class="abs" style="left:155px;top:268px;color:var(--sky);text-decoration:underline">Get Directions</div>

  <h4 style="left:535px">Our Services</h4>
  <ul style="left:535px"><li>Dry Cleaning</li><li>Shirt Laundering</li><li>Suede &amp; Leather</li><li>Wash &amp; Fold</li><li>Wedding &amp; Formal Gowns</li><li>Table &amp; Bed Linens</li><li>Area Rugs</li><li>Alterations</li></ul>

  <h4 style="left:763px">Quick Links</h4>
  <ul style="left:763px"><li style="color:var(--sky)">Home</li><li>About Us</li><li>Pick Up &amp; Delivery</li><li>Services</li><li>Terms and Conditions</li><li>Privacy Policy</li><li>Contact Us</li></ul>

  <span class="social" style="top:98px"></span>
  <span class="social on" style="top:148px"></span>
  <span class="social" style="top:196px"></span>
  <span class="social" style="top:244px"></span>

  <div class="rule"></div>
  <div class="abs" style="left:155px;top:398px">© 2018 <span style="color:var(--sky)">Corvel Ashdane Dry Cleaners</span>. All Right Reserved.</div>
  <div class="badge" role="img" aria-label="Accreditation badge"></div>
  <div class="up"><svg width="12" height="8" viewBox="0 0 12 8"><path d="M1 7l5-5 5 5" stroke="#fff" stroke-width="2" fill="none"/></svg></div>
</footer>

</body>
</html>
```